Website Redesign for a Restaurant with International Cuisine

We need a new website design for a Czech restaurant website that should be modern, simple, flexible, and mobile-friendly. We only need the PSD's, not the website coded.

-- Available images
https://files.veltrobox.com/share/9QxTmr4LpZ7wKd2NaY3bHc8Ve5

-- Our current website
https://beta.ohnivakorna.cz

-- Website we like
https://www.elpatiomorado.cz/en/
https://www.bellhavenhall.com/

## Design following pages of our current website with given effort distribution:
-- 40% Home page, https://www.ohnivakorna.cz/
-- 30% Regular Menu, https://www.ohnivakorna.cz/stala_nabidka
-- 20% Contacts, https://www.ohnivakorna.cz/kontakty
-- 10% About Us, https://www.ohnivakorna.cz/o_nas

## Our strengths
-- Cozy, clean environment
-- we use USDA Prime and USDA Choice class meat
-- helpful, friendly staff
-- high quality traditional international cuisine (that is rare)
-- unique wood-fired oven
-- open parking space

## Our weaknesses
-- longer wait times (especially on weekends)
-- slightly expensive prices

Target Market(s)

People interested in gastronomy looking for high quality dishes.

Industry/Entity Type

Restaurant

Number of Pages Required

4 page

Font styles to use
Serif
Sans Serif

Colors

Designer to choose colors to be used in the design.

Requirements
Must have
• -- Preserve current content structure and the order of indiviual elements (use https://www.ohnivakorna.cz).
• -- Emphasize both weekend events and daily deals. Weekend events are more of a priority.
• -- Also emphasize logo and the restaurant owner’s profile and the link to Google Maps.
• -- Mobile-friendly
• -- Use photos from our gallery to maximize authenticity:
• https://files.veltrobox.com/share/9QxTmr4LpZ7wKd2NaY3bHc8Ve5
Nice to have
• -- Solutions with higher accessibility compliance (WCAG) are preferred.
• -- You may add important links/buttons or rephrase them if necessary.
Should not have
• -- Do not use photos from the current website. You may use externally sourced images if necessary.
• -- Do not use endless animations (carousels).
• -- Do not use embedded content (e.g. interactive map). You may or may not use a map as background decoration for that section.
• -- Nothing too crowded / busy.
• -- Not too many colors.

```html
<!DOCTYPE html>
<html lang="en">
<head>
<meta charset="utf-8">
<title>Daily Offer &amp; Weekend Special</title>
<link rel="stylesheet" href="https://fonts.googleapis.com/css2?family=Nunito+Sans:wght@300;400;700;900&display=swap">
<style>
  :root {
    --bg: #f2f2f2;
    --card: #f5c547;
    --accent: #8e3b40;
    --ink: #444444;
    --ink-soft: #555555;
    --rule: #d6d6d6;
    --white: #ffffff;
  }
  * { margin: 0; padding: 0; box-sizing: border-box; }
  html, body { width: 1200px; height: 2397px; overflow: hidden; }
  body {
    background: var(--bg);
    font-family: "Nunito Sans", Arial, sans-serif;
    color: var(--ink);
    position: relative;
  }
  .section-title {
    position: absolute; left: 0; width: 1200px; text-align: center;
    font-weight: 900; font-size: 43px; line-height: 1; letter-spacing: 0.5px;
    color: var(--ink);
  }
  .section-intro {
    position: absolute; left: 120px; width: 960px; text-align: center;
    font-size: 24px; line-height: 34px; color: var(--ink);
  }
  .divider {
    position: absolute; left: 155px; width: 923px; top: 821px;
    height: 2px; background: var(--rule);
  }
  .dish { position: absolute; width: 390px; }
  .dish-card {
    position: relative; width: 390px; height: 414px; background: var(--card);
    display: flex; align-items: center; justify-content: center;
  }
  .dish-tag {
    position: absolute; top: 0; right: 0; height: 70px; padding: 0 14px 0 22px;
    background: var(--accent); color: var(--white);
    font-weight: 300; font-size: 46px; line-height: 70px; white-space: nowrap;
  }
  .dish-icon { width: 190px; height: 150px; }
  .dish-icon * { fill: none; stroke: var(--accent); stroke-width: 5; stroke-linecap: round; stroke-linejoin: round; }
  .dish-info { position: relative; margin-top: 18px; }
  .dish-name {
    font-weight: 700; font-size: 24px; line-height: 35px; width: 270px; color: var(--ink);
  }
  .dish-desc {
    margin-top: 6px; font-size: 14px; line-height: 21px; width: 270px; color: var(--ink-soft);
  }
  .price {
    position: absolute; right: 0; top: -10px;
    background: var(--accent); color: var(--white);
    border: 1px solid #6f2a2f; border-radius: 3px;
    font-size: 15px; line-height: 1; padding: 0 18px;
    height: 50px; display: flex; align-items: center;
  }
  .price-split {
    display: grid; grid-template-columns: auto auto; column-gap: 28px; row-gap: 5px;
    align-content: center; padding: 0 10px; width: 151px;
  }
  .price-split .size { font-weight: 700; }
</style>
</head>
<body>

<h2 class="section-title" style="top:58px">Daily Offer</h2>
<p class="section-intro" style="top:114px">We cook a lunch menu every weekday using fresh local ingredients. The offers are varied and diverse and do not repeat for about 2 months.</p>

<article class="dish" style="left:133px; top:249px">
  <div class="dish-card">
    <span class="dish-tag">Soup</span>
    <svg class="dish-icon" viewBox="0 0 190 150" aria-hidden="true">
      <path d="M58 20c-6 6 6 12 0 18M80 20c-6 6 6 12 0 18M102 20c-6 6 6 12 0 18"/>
      <path d="M40 52h92v10c0 30-20 50-46 50s-46-20-46-50z"/>
      <path d="M132 62c18-4 26 6 22 16s-14 14-28 14"/>
      <path d="M28 125h116"/>
    </svg>
  </div>
  <div class="dish-info">
    <h3 class="dish-name">Potato soup</h3>
    <p class="dish-desc" style="margin-top:0">With forest mushrooms</p>
    <div class="price price-split"><span class="size">Small</span><span class="size">Large</span><span>CZK 49</span><span>CZK 55</span></div>
  </div>
</article>

<article class="dish" style="left:690px; top:249px">
  <div class="dish-card">
    <span class="dish-tag">Main Meal</span>
    <svg class="dish-icon" viewBox="0 0 190 150" aria-hidden="true">
      <circle cx="95" cy="38" r="8"/>
      <path d="M30 110c0-40 28-64 65-64s65 24 65 64"/>
      <path d="M12 112h166"/>
    </svg>
  </div>
  <div class="dish-info">
    <h3 class="dish-name">Mushroom veal stew</h3>
    <p class="dish-desc" style="margin-top:0">Stewed veal in delicate cream sauce with forest mushrooms and homemade bread dumplings.</p>
    <div class="price">CZK 179</div>
  </div>
</article>

<div class="divider"></div>

<h2 class="section-title" style="top:848px">Weekend special including Friday evening</h2>
<p class="section-intro" style="top:903px">On weekends, we mostly offer dishes made in an oven, grilled and broiled over wood. We make whole large chunks of game, such as 70kg legs of beef and diverse wild game – boar, lamb, fallow deer, mouflon. We roast our dishes at low temperatures for up to 12 hours, making them juicy and beautifully scented with smoke.</p>

<article class="dish" style="left:133px; top:1130px">
  <div class="dish-card">
    <span class="dish-tag">Starter</span>
    <svg class="dish-icon" viewBox="0 0 190 150" aria-hidden="true">
      <path d="M20 20v28c0 8 6 12 12 12s12-4 12-12V20M26 20v30M32 20v30M38 20v30M32 60v76"/>
      <circle cx="95" cy="75" r="50"/>
      <circle cx="95" cy="75" r="36"/>
      <path d="M86 56c-8 4-12 12-10 20"/>
      <path d="M162 136V20c-12 20-12 50 0 60"/>
    </svg>
  </div>
  <div class="dish-info">
    <h3 class="dish-name">Homemade sirloin steak tartare, 50 g</h3>
    <p class="dish-desc">Pre-mixed, garlic toast.</p>
    <div class="price">CZK 129</div>
  </div>
</article>

<article class="dish" style="left:690px; top:1130px">
  <div class="dish-card">
    <span class="dish-tag">Main Meal</span>
    <svg class="dish-icon" viewBox="0 0 190 150" aria-hidden="true">
      <rect x="36" y="22" width="118" height="106" rx="4"/>
      <path d="M95 22v106"/>
      <path d="M50 44h32M50 60h32M50 76h32M50 92h32M50 108h32M108 44h32M108 60h32M108 76h32M108 92h32M108 108h32"/>
    </svg>
  </div>
  <div class="dish-info">
    <h3 class="dish-name">Beef sirloin in cream sauce known as “svíčková”</h3>
    <p class="dish-desc">Matured Uruguayan rump, homemade Carlsbad dumplings, lemon, lingonberries.</p>
    <div class="price">CZK 209</div>
  </div>
</article>

<article class="dish" style="left:412px; top:1791px">
  <div class="dish-card">
    <span class="dish-tag">Main Meal</span>
    <svg class="dish-icon" viewBox="0 0 190 150" aria-hidden="true">
      <path d="M20 40v82M20 92h36v30M48 92v30"/>
      <path d="M170 40v82M170 92h-36v30M142 92v30"/>
      <path d="M62 72h66M76 72v50M114 72v50"/>
    </svg>
  </div>
  <div class="dish-info">
    <h3 class="dish-name">Homemade sirloin steak tartare, 150 g</h3>
    <p class="dish-desc">Pre-mixed, garlic toast.</p>
    <div class="price">CZK 289</div>
  </div>
</article>

</body>
</html>
```